Digital Media Services Brochure

There are four services Lumen offers; web design, email marketing, social media and search engine optimization (SEO)

For now, we are looking only to design the Web Design piece. It will be the first of 4 similar designs, so keep in mind the actual design work has to carry over to other pages and be cohesive.

Lumen offers 4 services and each service has its own color. We would like a graphic representing all four services with coordinating colors. Since we are doing the Web Design page right now, blue should be used throughout the piece to differentiate it as the Web Design marketing piece.

Services and colors:
• Web Design = blue
• Social Media = pink
• SEO = green
• Email = gray

Web Design: Front Page Includes

The Lumen Advantage
• Increase Revenue
• Look Professional
• Reduce Expenses
• Attract Talent
• Creative

An area for 2 image examples (screenshots of work)

Lumen Information
• Facebook Icon and “facebook.com/LumenKV”
• Twitter Icon and “@LumenKV”
• Website: lumenkv.example
• Phone Number: 555.214.7093

Web Design: Back Page Includes

What’s next?
• Design consult
• Content creation
• Optimization
• Test/launch
• Marketing

Space for a testimonial and a photo

Space for a small quote or random fact

We want to show off some of our current clients so it should say “Some of our stellar clients” then show four client logos that are attached.

Target Market(s)

Marketing Directors of medium sized businesses which undertand and appreciate the value of digital media and how it drives business today.

Industry/Entity Type

Marketing

Requirements
Must have
• Similar feel of the Lumen website: lumenkv.example but doesn't need to be exactly the same, we are looking for a new design after all.

Include:
Facebook Icon with facebook.com/LumenKV
Twitter Icon with @LumenKV
Website: lumenkv.example
Phone Number: 555.214.7093
Nice to have
• Fun, trendy and clean design integrating the four Lumen colors.

```html
<!DOCTYPE html>
<html lang="en">
<head>
<meta charset="utf-8">
<title>Lumen – Web Design</title>
<link href="https://fonts.googleapis.com/css2?family=Comfortaa:wght@400;700&family=Questrial&family=Arimo&display=swap" rel="stylesheet">
<style>
  :root{
    --sky:#2a9ad3;
    --deep:#0a4f7c;
    --night:#03121c;
    --panel:#1f8cc4;
    --panel-edge:#36a6da;
    --accent:#f6a900;
    --white:#ffffff;
    --ink:#0b2330;
    --thumb-edge:#c8ccd0;
  }
  *{margin:0;padding:0;box-sizing:border-box}
  html,body{width:846px;height:1200px;overflow:hidden;background:var(--night)}
  .brochure{
    position:relative;width:846px;height:1200px;overflow:hidden;
    background:linear-gradient(180deg,#1b8cca 0%,#1a86c2 30%,#0f6797 52%,#08395a 66%,#05203a 80%,var(--night) 100%);
    font-family:"Comfortaa",sans-serif;color:var(--white);
  }
  .backdrop{position:absolute;inset:0}
  .top-band{position:absolute;left:0;top:0;width:846px;height:86px;background:rgba(4,40,70,.28)}
  .brand{position:absolute;left:20px;top:22px;display:flex;align-items:center;gap:12px}
  .brand-dot{width:40px;height:40px;border-radius:50%;background:var(--night)}
  .brand-name{font-family:"Comfortaa",sans-serif;font-weight:700;font-size:40px;color:var(--night);letter-spacing:.5px}
  .service-title{
    position:absolute;left:30px;top:168px;font-family:"Questrial",sans-serif;font-weight:400;
    font-size:72px;line-height:1;color:#eef3f6;transform:rotate(12deg);transform-origin:left top;
    text-shadow:0 3px 6px rgba(0,30,60,.35);white-space:nowrap;
  }
  .section-head{position:absolute;display:flex;align-items:center;gap:8px;font-weight:700;white-space:nowrap}
  .section-head .hl{color:var(--accent)}
  .next-head{left:24px;top:382px;font-size:38px}
  .next-mark{width:26px;height:26px;border:3px solid #cfe3ef;border-radius:50%;margin-right:12px}
  .steps{position:absolute;left:97px;top:455px;list-style:none}
  .steps li{display:flex;align-items:center;gap:8px;height:27px;font-size:19px;white-space:nowrap}
  .quote-head{left:419px;top:492px;font-size:21px}
  .chev{width:20px;height:16px}
  .quote-art{position:absolute;left:378px;top:542px;width:70px;height:60px;border-radius:4px;
    background:linear-gradient(135deg,#e9e6d8,#b9c88a)}
  .quote-text{position:absolute;left:455px;top:550px;width:360px;font-size:11.5px;line-height:19px;color:var(--ink);font-weight:700}
  .quote-text .hl{color:var(--accent)}
  .quote-text .line{display:block;white-space:nowrap}
  .quote-text .line + .line{padding-left:4px}
  .quote-by{position:absolute;left:664px;top:604px;font-size:12px;font-weight:700;white-space:nowrap}
  .panel{position:absolute;left:21px;width:804px;height:203px;border-radius:6px;background:var(--panel);
    box-shadow:inset 0 0 0 1px var(--panel-edge)}
  .testimonial{top:663px}
  .clients{top:878px}
  .panel .section-head{left:28px;top:12px;font-size:21px}
  .photo-stack{position:absolute;left:52px;top:52px;width:134px;height:134px}
  .photo-back{position:absolute;inset:0;background:#0d5f8a;transform:rotate(-4deg)}
  .photo{position:absolute;inset:4px;border:5px solid #050a0d;transform:rotate(6deg);
    background:linear-gradient(160deg,#d9b58d,#7a8a8f)}
  .testimonial-copy{position:absolute;left:218px;top:66px;width:570px;font-size:11px;line-height:17px;font-weight:700}
  .testimonial-copy p{margin-bottom:17px}
  .testimonial-copy .sign{position:absolute;right:22px;top:91px;margin:0}
  .thumbs{position:absolute;left:43px;top:59px;display:flex;gap:12px}
  .thumb{width:172px;height:122px;border-radius:6px;border:3px solid var(--thumb-edge)}
  .t1{background:linear-gradient(135deg,#f4f6f7,#b9c3c9)}
  .t2{background:linear-gradient(135deg,#ffffff,#6fb5dc)}
  .t3{background:linear-gradient(135deg,#f2f6f8,#c9dbb4)}
  .t4{background:linear-gradient(135deg,#58b33c,#2c5a1e)}
  .footer{position:absolute;left:0;top:1155px;width:846px;height:45px;background:rgba(0,0,0,.35);
    padding:6px 0 0 22px;font-family:"Arimo",sans-serif;font-size:13.5px;line-height:16px}
</style>
</head>
<body>
<main class="brochure">
  <svg class="backdrop" width="846" height="1200" viewBox="0 0 846 1200" aria-hidden="true">
    <defs>
      <linearGradient id="ray" x1="0" x2="1">
        <stop offset="0" stop-color="#6fd0f0" stop-opacity="0"/>
        <stop offset=".5" stop-color="#6fd0f0" stop-opacity=".28"/>
        <stop offset="1" stop-color="#6fd0f0" stop-opacity="0"/>
      </linearGradient>
      <linearGradient id="swoosh" x1="0" y1="0" x2="1" y2="1">
        <stop offset="0" stop-color="#5fc0ec" stop-opacity=".55"/>
        <stop offset="1" stop-color="#1a86c2" stop-opacity="0"/>
      </linearGradient>
      <linearGradient id="hill" x1="0" y1="0" x2="0" y2="1">
        <stop offset="0" stop-color="#2aa5c8" stop-opacity=".55"/>
        <stop offset="1" stop-color="#0a3e60" stop-opacity="0"/>
      </linearGradient>
    </defs>
    <rect x="330" y="90" width="200" height="560" fill="url(#ray)"/>
    <rect x="440" y="90" width="110" height="560" fill="url(#ray)"/>
    <path d="M0 165 C140 260 300 320 440 335 L440 360 C280 350 120 300 0 230 Z" fill="url(#swoosh)"/>
    <path d="M0 165 C140 260 300 320 440 335" stroke="#bfe6f7" stroke-opacity=".6" stroke-width="2" fill="none"/>
    <path d="M390 520 C520 440 720 430 846 470 L846 660 L390 660 Z" fill="url(#hill)"/>
    <path d="M390 520 C520 440 720 430 846 470" stroke="#8fd6ec" stroke-opacity=".5" stroke-width="1.5" fill="none"/>
  </svg>

  <div class="top-band"></div>
  <div class="brand"><span class="brand-dot"></span><span class="brand-name">Lumen</span></div>

  <h1 class="service-title">Web Design</h1>

  <h2 class="section-head next-head"><span class="next-mark"></span><span class="hl">What’s</span> Next</h2>
  <ul class="steps">
    <li><svg width="20" height="18" viewBox="0 0 20 18"><path d="M2 10 L8 15 L18 2" stroke="#f6a900" stroke-width="4" fill="none" stroke-linecap="round" stroke-linejoin="round"/></svg>Design consult</li>
    <li><svg width="20" height="18" viewBox="0 0 20 18"><path d="M2 10 L8 15 L18 2" stroke="#f6a900" stroke-width="4" fill="none" stroke-linecap="round" stroke-linejoin="round"/></svg>Content creation</li>
    <li><svg width="20" height="18" viewBox="0 0 20 18"><path d="M2 10 L8 15 L18 2" stroke="#f6a900" stroke-width="4" fill="none" stroke-linecap="round" stroke-linejoin="round"/></svg>Optimization</li>
    <li><svg width="20" height="18" viewBox="0 0 20 18"><path d="M2 10 L8 15 L18 2" stroke="#f6a900" stroke-width="4" fill="none" stroke-linecap="round" stroke-linejoin="round"/></svg>Test/launch</li>
    <li><svg width="20" height="18" viewBox="0 0 20 18"><path d="M2 10 L8 15 L18 2" stroke="#f6a900" stroke-width="4" fill="none" stroke-linecap="round" stroke-linejoin="round"/></svg>Marketing</li>
  </ul>

  <h2 class="section-head quote-head">
    <svg class="chev" viewBox="0 0 20 16"><path d="M2 2 L8 8 L2 14 M10 2 L16 8 L10 14" stroke="#fff" stroke-width="3" fill="none"/></svg>
    <span class="hl">Quote</span> Ex.
  </h2>
  <div class="quote-art" role="img" aria-label="Illustration of a note page with a quill"></div>
  <p class="quote-text">
    <span class="line">“ Social media isn’t a fad. <span class="hl">It’s a Fundamental shift</span> in the way</span>
    <span class="line">we communicate”</span>
  </p>
  <p class="quote-by">-Social lumen media</p>

  <section class="panel testimonial">
    <h2 class="section-head">
      <svg class="chev" viewBox="0 0 20 16"><path d="M2 2 L8 8 L2 14 M10 2 L16 8 L10 14" stroke="#fff" stroke-width="3" fill="none"/></svg>
      <span><span class="hl">Testi</span>monial</span>
    </h2>
    <div class="photo-stack">
      <div class="photo-back"></div>
      <div class="photo" role="img" aria-label="Client photo"></div>
    </div>
    <div class="testimonial-copy">
      <p>“ Testimonial from some of our clients will go in this space. “</p>
      <p>“There are many variations of passages of Lorem Ipsum available, but the majority have suffered alteration in some form, by injected humour, or randomised words which<br>don’t look even slightly”</p>
      <p class="sign">- Client</p>
    </div>
  </section>

  <section class="panel clients">
    <h2 class="section-head">
      <svg class="chev" viewBox="0 0 20 16"><path d="M2 2 L8 8 L2 14 M10 2 L16 8 L10 14" stroke="#fff" stroke-width="3" fill="none"/></svg>
      <span><span class="hl">Some of our</span> Stellar Clients</span>
    </h2>
    <div class="thumbs">
      <div class="thumb t1" role="img" aria-label="Client work: laptop product image"></div>
      <div class="thumb t2" role="img" aria-label="Client work: blue butterfly design artwork"></div>
      <div class="thumb t3" role="img" aria-label="Client work: fruit splashing in water"></div>
      <div class="thumb t4" role="img" aria-label="Client work: web design portfolio screen"></div>
    </div>
  </section>

  <footer class="footer">
    <p>Website: www.lumenkv.example</p>
    <p>Phone Number: 555.214.7093</p>
  </footer>
</main>
</body>
</html>
```